Harbor of Mercy - Team of Rabbis and Doctors Helping Families Dealing with Illness

The Harbor of Mercy is an organization that accompanies families dealing with severe illnesses of a family member. A team of rabbis and doctors provide support and real-time responses to these families.
The site theme is medicine and law, but the target market is religious Jewish families in crisis. Thus, the site design needs to combine:
- professional, conservative, serious
- spiritual
- warm hug

Target Market(s)

religious families suffering a health crisis

Industry/Entity Type

Non-profit organization

Number of Pages Required

1 page

Font styles to use
Sans Serif

Requirements
Must have
• Final design in PSD format. List of fonts used, colors used and link/button colors used in the design.

```html
<!DOCTYPE html>
<html lang="en">
<head>
<meta charset="utf-8">
<title>Harbor of Mercy</title>
<link href="https://fonts.googleapis.com/css2?family=Montserrat:wght@400;500;600;700;800&display=swap" rel="stylesheet">
<style>
:root{
  --navy:#0b2a5b;
  --navy-deep:#08214a;
  --cyan:#1aa3dc;
  --cyan-bright:#14a9e6;
  --text:#3d3d3d;
  --muted:#9a9a9a;
  --grey-band:#f1f1f1;
  --white:#ffffff;
  --star:#f4a71c;
}
*{margin:0;padding:0;box-sizing:border-box}
html,body{width:1200px;height:4747px;overflow:hidden}
body{position:relative;background:var(--white);font-family:"Montserrat",sans-serif;color:var(--text)}
.abs{position:absolute}
.topbar{left:0;top:0;width:1200px;height:52px;background:var(--navy);color:var(--white);font-size:13px}
.topbar .item{position:absolute;top:18px;display:flex;align-items:center;gap:6px}
.topbar .sep{position:absolute;top:12px;width:1px;height:28px;background:rgba(255,255,255,.35)}
.search{position:absolute;left:901px;top:12px;width:189px;height:28px;border-radius:14px;background:var(--white);color:#888;font-size:12px;padding:7px 0 0 20px}
.nav{left:0;top:52px;width:1200px;height:114px;background:var(--white)}
.nav a{position:absolute;top:48px;font-size:14px;color:#444;text-decoration:none}
.brand{position:absolute;left:886px;top:38px;display:flex;align-items:center;gap:10px;font-size:21px;font-weight:700;color:var(--navy)}
.brand .mark{width:16px;height:16px;border-radius:50%;background:var(--cyan)}
.hero{left:0;top:166px;width:1200px;height:601px;background:radial-gradient(ellipse at 45% 40%,#6e5537 0%,#3b2c1c 45%,#1b140d 100%)}
.hero h1{position:absolute;left:0;top:232px;width:1200px;text-align:center;color:var(--white);font-size:50px;font-weight:700;line-height:66px;letter-spacing:.5px;text-shadow:0 2px 8px rgba(0,0,0,.5)}
.arrow{position:absolute;width:22px;height:22px;border-radius:50%;background:var(--cyan)}
.photo{position:absolute}
h2.section{position:absolute;font-size:34px;font-weight:700;color:#1a1a1a;letter-spacing:.3px}
.para{position:absolute;width:490px;font-size:14.5px;line-height:30px;color:#444}
.btn{position:absolute;background:var(--cyan);color:var(--white);font-size:14px;font-weight:700;border-radius:6px;display:flex;align-items:center;justify-content:center;letter-spacing:.3px}
.play{position:absolute;left:478px;top:1250px;width:76px;height:76px;border-radius:50%;background:var(--white);border:4px solid var(--cyan);display:flex;align-items:center;justify-content:center}
.play span{width:62px;height:62px;border-radius:50%;background:var(--navy);display:flex;align-items:center;justify-content:center}
.services{left:0;top:1972px;width:1200px;height:428px;background:var(--grey-band)}
.card{position:absolute;top:87px;width:223px;height:265px;overflow:hidden;border-radius:4px}
.card .label{position:absolute;left:0;bottom:0;width:223px;height:66px;background:var(--cyan-bright);border-radius:60% 60% 4px 4px / 40% 40% 4px 4px;color:var(--white);font-weight:700;font-size:15px;text-align:center;padding-top:30px}
.card.conf{background:var(--navy);color:var(--white);text-align:center;padding:28px 20px 0}
.card.conf h3{font-size:15px;font-weight:700;margin-bottom:10px}
.card.conf p{font-size:11px;line-height:20px}
.card.conf .small{display:inline-block;margin-top:14px;background:var(--cyan);border-radius:10px;font-size:9px;font-weight:700;padding:5px 18px}
.testi-text{position:absolute;font-size:14px;line-height:30px;text-align:center}
.blog-card{position:absolute;background:var(--white);box-shadow:0 4px 18px rgba(0,0,0,.1)}
.blog-card h4{font-size:21px;font-weight:700;color:#1a1a1a;margin-bottom:14px}
.blog-card p{font-size:13.5px;line-height:26px;color:#444}
.blog-card .more{font-size:13px;font-weight:700;color:var(--cyan);margin-top:8px}
.rabbi{left:0;top:3627px;width:1200px;height:243px}
.newsletter{left:116px;top:3962px;width:968px;height:257px;background:var(--navy);border-radius:4px}
.footer{left:0;top:4260px;width:1200px;height:487px;background:linear-gradient(180deg,#ffffff 0%,#f3f7fb 55%,#e6eef6 100%)}
.footer a{position:absolute;top:285px;font-size:14px;color:#333;text-decoration:none}
.social{position:absolute;top:400px;width:44px;height:44px;border-radius:50%;border:1.5px solid #cfdcec;background:var(--white)}
</style>
</head>
<body>

<!-- Top bar -->
<div class="abs topbar">
  <div class="item" style="left:110px"><svg width="12" height="12" viewBox="0 0 24 24"><path fill="#fff" d="M6.6 10.8a15 15 0 006.6 6.6l2.2-2.2c.3-.3.7-.4 1-.2 1.1.4 2.3.6 3.6.6.6 0 1 .4 1 1V20c0 .6-.4 1-1 1A17 17 0 013 4c0-.6.4-1 1-1h3.5c.6 0 1 .4 1 1 0 1.3.2 2.5.6 3.6.1.3 0 .7-.2 1z"/></svg>+1 555 010 2040</div>
  <div class="sep" style="left:255px"></div>
  <div class="item" style="left:268px"><svg width="13" height="11" viewBox="0 0 24 18"><rect x="1" y="1" width="22" height="16" rx="2" fill="#fff"/><path d="M2 2l10 8 10-8" stroke="#0b2a5b" stroke-width="2" fill="none"/></svg>info@harborofmercy.org</div>
  <div class="sep" style="left:470px"></div>
  <div class="item" style="left:484px"><svg width="12" height="12" viewBox="0 0 24 24"><path fill="#fff" d="M10 17l5-5-5-5v3H2v4h8zM14 3h6a2 2 0 012 2v14a2 2 0 01-2 2h-6v-2h6V5h-6z"/></svg>Login</div>
  <div class="sep" style="left:560px"></div>
  <div class="item" style="left:584px"><span style="width:8px;height:8px;border-radius:50%;background:#fff;display:block"></span></div>
  <div class="sep" style="left:618px"></div>
  <div class="item" style="left:642px">Dedication 2</div>
  <div class="sep" style="left:754px"></div>
  <div class="item" style="left:779px">Dedication 1</div>
  <div class="sep" style="left:882px"></div>
  <div class="search">Search
    <svg style="position:absolute;right:12px;top:8px" width="12" height="12" viewBox="0 0 24 24"><circle cx="10" cy="10" r="7" stroke="#1aa3dc" stroke-width="3" fill="none"/><path d="M15 15l6 6" stroke="#1aa3dc" stroke-width="3"/></svg>
  </div>
</div>

<!-- Navigation -->
<div class="abs nav">
  <a style="left:110px">Home</a>
  <a style="left:193px">About Us</a>
  <a style="left:303px">Our Services</a>
  <a style="left:436px">What We Offer</a>
  <a style="left:587px">Our Events</a>
  <a style="left:706px">Contact Us</a>
  <div class="brand"><span class="mark"></span>Harbor of Mercy</div>
</div>

<!-- Hero -->
<div class="abs hero" role="img" aria-label="Family gathered around lit candles in a warm room">
  <h1>SHOULD MORPHINE BE GIVEN<br>TO THE PATIENT?</h1>
  <div class="arrow" style="left:48px;top:297px"><svg width="22" height="22" viewBox="0 0 22 22"><path d="M13 7l-4 4 4 4" stroke="#fff" stroke-width="2" fill="none"/></svg></div>
  <div class="arrow" style="left:1130px;top:297px"><svg width="22" height="22" viewBox="0 0 22 22"><path d="M9 7l4 4-4 4" stroke="#fff" stroke-width="2" fill="none"/></svg></div>
</div>

<!-- About -->
<div class="photo" style="left:111px;top:837px;width:411px;height:466px;background:radial-gradient(ellipse at 60% 55%,#c0843e 0%,#6b4522 45%,#261a10 100%)" role="img" aria-label="Elderly rabbi and young girl lighting candles"></div>
<div class="play"><span><svg width="18" height="20" viewBox="0 0 18 20"><path d="M3 2l13 8-13 8z" fill="#fff"/></svg></span></div>
<h2 class="section" style="left:588px;top:872px">ABOUT US</h2>
<p class="para" style="left:584px;top:931px">Lorem ipsum dolor sit amet, consectetur adipiscing elit, sed do eiusmod tempor incididunt ut labore et dolore magna aliqua. Quis ipsum suspendisse ultrices gravida. Risus commodo viverra maecenas accumsan lacus vel facilisis.</p>
<p class="para" style="left:584px;top:1081px">Lorem ipsum dolor sit amet, consectetur adipiscing elit, sed do eiusmod tempor incididunt ut labore et dolore magna aliqua. Quis ipsum suspendisse ultrices gravida. Risus commodo viverra maecenas accumsan lacus vel facilisis.</p>
<div class="btn" style="left:582px;top:1227px;width:166px;height:52px">LEARN MORE</div>

<!-- Moral issues -->
<h2 class="section" style="left:114px;top:1447px">MORE MORAL ISSUES</h2>
<p class="para" style="left:114px;top:1506px">Lorem ipsum dolor sit amet, consectetur adipiscing elit, sed do eiusmod tempor incididunt ut labore et dolore magna aliqua. Quis ipsum suspendisse ultrices gravida. Risus commodo viverra maecenas accumsan lacus vel facilisis.</p>
<p class="para" style="left:114px;top:1656px">Lorem ipsum dolor sit amet, consectetur adipiscing elit, sed do eiusmod tempor incididunt ut labore et dolore magna aliqua. Quis ipsum suspendisse ultrices gravida. Risus commodo viverra maecenas accumsan lacus vel facilisis.</p>
<div class="btn" style="left:112px;top:1802px;width:166px;height:52px">LEARN MORE</div>
<div class="abs" style="left:899px;top:1386px;width:210px;height:228px;background:var(--navy)"></div>
<div class="photo" style="left:675px;top:1410px;width:411px;height:466px;background:radial-gradient(ellipse at 55% 60%,#d09a55 0%,#7a5330 45%,#2c1f15 100%)" role="img" aria-label="Grandmother and children by lit candles"></div>
<div class="abs" style="left:662px;top:1699px;width:191px;height:190px;border:2px solid var(--cyan)"></div>

<!-- Services -->
<div class="abs services">
  <div class="card" style="left:112px;background:linear-gradient(160deg,#d8dde2,#8b939b)" role="img" aria-label="Students raising hands in a classroom"><div class="label">COURSES</div></div>
  <div class="card conf" style="left:361px">
    <h3>CONFERENCES</h3>
    <p>Lorem ipsum dolor sit amet, consectetur adipiscing elit, sed do eiusmod tempor incididunt ut labore et dolore magna aliqua. Quis ipsum suspendisse ultrices</p>
    <span class="small">Learn More</span>
  </div>
  <div class="card" style="left:612px;background:linear-gradient(160deg,#b8c7d3,#3e5366)" role="img" aria-label="Speaker addressing a lecture hall audience"><div class="label">LECTURES</div></div>
  <div class="card" style="left:861px;background:linear-gradient(160deg,#2f8fc0,#1c4f7c)" role="img" aria-label="Support 24 hours hotline graphic"><div class="label">HOTLINE 24/7</div></div>
</div>

<!-- Testimonials -->
<h2 class="section" style="left:0;top:2460px;width:1200px;text-align:center">CLIENT TESTIMONIALS</h2>
<div class="abs" style="left:582px;top:2540px;width:50px;height:50px;border-radius:50%;background:linear-gradient(#cfcfcf,#7d7d7d)" role="img" aria-label="Client portrait"></div>
<div class="abs" style="left:0;top:2606px;width:1200px;text-align:center;color:var(--star);font-size:16px;letter-spacing:2px">★★★★★</div>
<p class="testi-text" style="left:0;top:2657px;width:220px;color:#b3b3b3;text-align:left">o eiusmod tempor incididunt ut<br>gravida. Risus commodo viver-<br>ilisis.</p>
<p class="testi-text" style="left:280px;top:2657px;width:660px;color:#333">Lorem ipsum dolor sit amet, consectetur adipiscing elit, sed do eiusmod tempor incididunt ut labore et dolore magna aliqua. Quis ipsum suspendisse ultrices gravida. Risus commodo viverra maecenas accumsan lacus vel facilisis.</p>
<p class="testi-text" style="left:1000px;top:2662px;width:220px;color:#b3b3b3;text-align:left">Lorem ipsum dolor sit amet<br>labore et dolore magna aliqu<br><span style="padding-left:186px">ra</span></p>
<div class="abs" style="left:0;top:2772px;width:1200px;text-align:center;font-size:20px;font-weight:600;color:#222">Daniel Reed</div>
<div class="abs" style="left:0;top:2810px;width:1200px;text-align:center;font-size:14px;color:#444">Dec 14,2023</div>
<div class="abs" style="left:293px;top:2868px;width:634px;height:4px;background:#d6d6d6"></div>
<div class="abs" style="left:522px;top:2867px;width:178px;height:6px;background:var(--cyan)"></div>

<!-- Blog -->
<h2 class="section" style="left:0;top:2994px;width:1200px;text-align:center">OUR BLOG</h2>
<div class="abs arrow" style="left:41px;top:3288px"><svg width="22" height="22" viewBox="0 0 22 22"><path d="M13 7l-4 4 4 4" stroke="#fff" stroke-width="2" fill="none"/></svg></div>
<div class="abs arrow" style="left:1130px;top:3288px;background:#e4e4e4"><svg width="22" height="22" viewBox="0 0 22 22"><path d="M9 7l4 4-4 4" stroke="#fff" stroke-width="2" fill="none"/></svg></div>

<div class="blog-card" style="left:109px;top:3262px;width:311px;height:269px;padding:58px 20px 0 20px">
  <h4>Lorem Ipsum</h4>
  <p>Lorem ipsum dolor sit amet, consectetur adipiscing elit, sed do eiusmod tempor incididunt ut labore et dolore magna aliqua. Quis ipsum suspendisse ultrices gravida.</p>
  <div class="more">Learn More</div>
</div>
<div class="photo" style="left:124px;top:3089px;width:280px;height:199px;background:linear-gradient(160deg,#e9ecef,#9aa3ab)" role="img" aria-label="Team meeting around a conference table"></div>

<div class="blog-card" style="left:442px;top:3089px;width:312px;height:442px;padding:26px 18px 0 18px">
  <h4>Lorem Ipsum</h4>
  <p>Lorem ipsum dolor sit amet, consectetur adipiscing elit, sed do eiusmod tempor incididunt ut labore et dolore magna aliqua. Quis ipsum suspendisse ultrices gravida.</p>
  <div class="more">Learn More</div>
</div>
<div class="photo" style="left:459px;top:3332px;width:280px;height:199px;background:linear-gradient(160deg,#8ea3b8,#2b3a4c)" role="img" aria-label="Speaker with microphone at a conference"></div>

<div class="blog-card" style="left:778px;top:3262px;width:311px;height:269px;padding:58px 20px 0 20px">
  <h4>Lorem Ipsum</h4>
  <p>Lorem ipsum dolor sit amet, consectetur adipiscing elit, sed do eiusmod tempor incididunt ut labore et dolore magna aliqua. Quis ipsum suspendisse ultrices gravida.</p>
  <div class="more">Learn More</div>
</div>
<div class="photo" style="left:793px;top:3089px;width:280px;height:199px;background:radial-gradient(ellipse at 50% 55%,#9a7346,#3b2a1a 70%,#1a120b)" role="img" aria-label="Elderly rabbi beside lit candles"></div>

<!-- Ask the Rabbi -->
<div class="abs rabbi">
  <svg class="abs" style="left:0;top:0" width="1200" height="243" viewBox="0 0 1200 243">
    <defs><linearGradient id="cyanBand" x1="0" x2="1"><stop offset="0" stop-color="#1aa3dc"/><stop offset="1" stop-color="#14a9e6"/></linearGradient></defs>
    <rect width="1200" height="243" fill="#0b2a5b"/>
    <polygon points="464,0 1200,0 1200,243 337,243" fill="url(#cyanBand)"/>
  </svg>
  <h2 class="section" style="left:114px;top:60px;color:#fff">ASK THE RABBI</h2>
  <div class="abs" style="left:112px;top:116px;width:133px;height:48px;background:#fff;border-radius:4px;color:var(--cyan);font-size:13px;font-weight:700;display:flex;align-items:center;justify-content:center">Learn More</div>
  <p class="abs" style="left:470px;top:60px;width:640px;font-size:13.5px;line-height:25px;color:#fff">Lorem ipsum dolor sit amet, consectetur adipiscing elit, sed do eiusmod tempor incididunt ut labore et dolore magna aliqua. Quis ipsum suspendisse ultrices gravida. Risus commodo viverra maecenas accumsan lacus vel facilisis. Lorem ipsum dolor sit amet, consectetur adipiscing elit, sed do eiusmod tempor incididunt ut labore et dolore magna aliqua.</p>
</div>

<!-- Newsletter -->
<div class="abs newsletter">
  <div class="abs" style="left:0;top:54px;width:968px;text-align:center;color:#fff;font-size:33px;font-weight:700;letter-spacing:.5px">SUBSCRIBE NEWSLETTER</div>
  <div class="abs" style="left:79px;top:124px;width:809px;height:52px;background:#fff;border-radius:26px;font-size:14px;color:#555;padding:16px 0 0 32px">Enter Your Email</div>
  <div class="abs" style="left:732px;top:124px;width:156px;height:52px;background:var(--cyan);border:3px solid #fff;border-radius:26px;color:#fff;font-size:15px;font-weight:700;display:flex;align-items:center;justify-content:center">Subscribe</div>
</div>

<!-- Footer -->
<div class="abs footer">
  <div class="abs" style="left:0;top:110px;width:1200px;display:flex;justify-content:center;align-items:center;gap:16px">
    <span style="width:26px;height:26px;border-radius:50%;background:var(--cyan)"></span>
    <span style="font-size:40px;font-weight:700;color:var(--navy)">Harbor of Mercy</span>
  </div>
  <a style="left:281px">Home</a>
  <a style="left:359px">About Us</a>
  <a style="left:462px">Our Services</a>
  <a style="left:588px">What We Offer</a>
  <a style="left:730px">Our Events</a>
  <a style="left:842px">Contact Us</a>
  <div class="abs" style="left:0;top:342px;width:1200px;text-align:center;font-size:13px;color:#333">Copyright© 2023 <span style="color:var(--cyan);text-decoration:underline">Harbor of Mercy</span> | All Rights Reserved</div>
  <div class="social" style="left:492px;background:var(--navy);border-color:var(--navy)" aria-label="Social link"></div>
  <div class="social" style="left:544px" aria-label="Social link"></div>
  <div class="social" style="left:595px" aria-label="Social link"></div>
  <div class="social" style="left:647px" aria-label="Social link"></div>
</div>

</body>
</html>
```